Web Design Project for DJ

We need a web design for a DJ. Our client is a freelance DJ who already has a regular gig at a major night club but is looking to expand his exposure. He is located in a major metropolitan area and is looking for further gigs. He is hoping to generate further business via the website, including bookings via the site.

For reference his pagelinker page is here https://www.pagelinker.example/pages/DJ-Vorn/730162948415207

Following face to face discussions with the client today we have made a few small alterations to the brief.  We are hoping to have some images uploaded shortly.

Target Market(s)

Event planners, night club owners, radio stations, younger age groups (16-35)

Industry/Entity Type

Business

Requirements
Must have
• Name is DJVorn, this should obviously feature prominently. His current business card is attached as an example.

Links to Pagelinker and Tunedrift

Cool, modern look, slightly edgy.

Site will be built in Joomla, so a front page and secondary page template is required.
Nice to have
• Blog style layout to front page featuring recent and upcoming gigs.

Secondary pages may include a more expansive blog, a list of upcoming gigs, and a booking form.

Darker colour palettes preferred and use of same/similar fonts to those on the business card are an obvious plus

```html
<!DOCTYPE html>
<html lang="en">
<head>
<meta charset="utf-8">
<title>dj vorn</title>
<link href="https://fonts.googleapis.com/css2?family=Arimo:wght@400;700&family=Gelasio:wght@700&display=swap" rel="stylesheet">
<style>
:root{
  --accent:#e0461f;
  --ink:#2b2b2b;
  --muted:#8a8a8a;
  --link:#3a66b8;
  --social:#3d5a98;
  --card-line:#dcdcdc;
  --dark:#2f2f2f;
}
*{margin:0;padding:0;box-sizing:border-box}
html,body{width:1022px;height:1200px;overflow:hidden}
body{position:relative;background:linear-gradient(#ececec 456px,#fafafa 560px,#f7f7f7);font-family:"Arimo",Arial,sans-serif;color:var(--ink)}
.abs{position:absolute}
.serif{font-family:"Gelasio",Georgia,serif;font-weight:700}

.hero{left:0;top:0;width:1022px;height:456px;background:#000}
.hero-photo{left:67px;top:84px;width:888px;height:372px;background:radial-gradient(ellipse at 70% 40%,#ff5a1e 0%,#c8261a 30%,#5a0c10 60%,#0a0203 90%)}
.nav-bar{left:214px;top:12px;width:731px;height:72px;background:#fff;border-radius:36px}
.logo{left:78px;top:24px;font-size:34px;line-height:40px;color:#fff;white-space:nowrap}
.logo-dot{left:214px;top:16px;width:64px;height:64px;border-radius:50%;background:#111;border:3px solid #fff}
.nav{right:99px;top:41px;display:flex;gap:31px;font-size:13px;text-transform:uppercase;white-space:nowrap}
.nav a{color:#111;text-decoration:none}
.nav a.current{color:var(--accent)}
.hero-caption{left:78px;top:403px;font-size:21px;font-weight:700;color:#fff;text-transform:uppercase;letter-spacing:-.5px;
  text-shadow:-1.5px 0 #000,1.5px 0 #000,0 -1.5px #000,0 1.5px #000}
.arrow{top:405px;width:22px;height:22px;border-radius:50%;background:#fff}
.arrow svg{display:block}

.welcome-title{left:77px;top:486px;font-size:25px;color:var(--accent)}
.welcome-text{left:77px;top:525px;width:618px;font-size:12px;line-height:19.6px;text-align:justify;color:#333}
.deck{left:722px;top:538px;width:223px;height:110px;border-radius:10px;background:linear-gradient(160deg,#5c5c5c,#2a2a2a)}
.rule{left:77px;top:682px;width:868px;height:1px;background:linear-gradient(90deg,transparent,#d6d6d6 20%,#d6d6d6 80%,transparent)}

.col-title{top:706px;font-size:18px;color:var(--accent)}
.col-title.social{color:var(--social)}
.view-all{top:712px;font-size:9px;color:var(--muted);display:flex;align-items:center;gap:6px}
.view-all i{display:inline-block;width:16px;height:16px;border-radius:50%;background:#8c8c8c;position:relative}
.view-all i:after{content:"";position:absolute;left:5px;top:5px;width:4px;height:4px;border-top:1.5px solid #fff;border-right:1.5px solid #fff;transform:rotate(45deg)}
.social-mark{left:682px;top:703px;width:23px;height:23px;background:var(--social);border-radius:3px}

.card{width:264px;height:96px;background:linear-gradient(#f6f6f6,#ebebeb);border:1px solid var(--card-line);border-radius:4px}
.thumb{left:14px;top:13px;width:71px;height:70px;border:3px solid #fff;box-shadow:0 1px 3px rgba(0,0,0,.3)}
.play{left:22px;top:24px;width:28px;height:22px;background:rgba(255,255,255,.75);border:1px solid #333;border-radius:2px}
.play:after{content:"";position:absolute;left:10px;top:5px;border-left:10px solid #222;border-top:6px solid transparent;border-bottom:6px solid transparent}
.card-text{left:97px;top:15px;font-size:11px;line-height:16px;color:#333;white-space:nowrap;letter-spacing:-.1px}
.card-text a{color:var(--link);text-decoration:none}
.card-date{left:97px;top:72px;font-size:11px;color:#111;white-space:nowrap}
.card-meta{left:97px;top:74px;font-size:8.5px;color:#111;white-space:nowrap}

.famous{left:76px;top:1054px;width:870px;height:55px;background:linear-gradient(#3c3c3c,#262626);border:1px solid #111;border-radius:3px}
.famous-label{left:0;top:0;width:137px;height:53px;background:linear-gradient(#4a4a4a,#333);font-size:18px;color:#f07a4e;display:flex;align-items:center;justify-content:center}
.famous-text{left:153px;top:19px;font-size:13px;color:#fff;white-space:nowrap}
.player{left:528px;top:12px;width:178px;height:28px;background:#111;border:2px solid #555;border-radius:2px}
.player-time{left:100px;top:7px;font-size:10px;color:#fff;white-space:nowrap}
.player-time span{color:#aaa}
.btn{top:12px;height:29px;background:linear-gradient(#fff,#e4e4e4);border:1px solid #bbb;font-size:10px;font-weight:700;color:#666;display:flex;align-items:center;justify-content:center;gap:5px}
.btn b{display:inline-block;width:9px;height:9px;background:#5b7bc0;border-radius:2px}

.footer{left:0;top:1124px;width:1022px;height:76px;background:linear-gradient(#333,#2a2a2a)}
.footer-links{left:76px;top:17px;font-size:13px;color:#bbb;word-spacing:3px;white-space:nowrap}
.footer-copy{left:76px;top:43px;font-size:13px;color:#bbb;word-spacing:3px;white-space:nowrap}
.footer-icon{top:29px;width:22px;height:22px;border-radius:4px}
</style>
</head>
<body>

<header class="abs hero">
  <div class="abs hero-photo" role="img" aria-label="DJ in a hat working the mixing deck under red club lights"></div>
  <div class="abs nav-bar"></div>
  <div class="abs logo-dot"></div>
  <div class="abs logo serif">dj vorn</div>
  <nav class="abs nav">
    <a class="current" href="#">Home</a><a href="#">About us</a><a href="#">Gigs</a><a href="#">Contact us</a>
  </nav>
  <div class="abs hero-caption">Nullam nisl enim, fermentum</div>
  <div class="abs arrow" style="left:892px"><svg width="22" height="22"><path d="M16 11H6M10 7l-4 4 4 4" stroke="#f08a2a" stroke-width="1.6" fill="none"/></svg></div>
  <div class="abs arrow" style="left:923px"><svg width="22" height="22"><path d="M6 11h10M12 7l4 4-4 4" stroke="#f08a2a" stroke-width="1.6" fill="none"/></svg></div>
</header>

<h1 class="abs welcome-title serif">Welcome to dj vorn</h1>
<p class="abs welcome-text">Cras sit amet est et nisl faucibus venenatis non at magna. Maecenas tincidunt mi in nunc dignissim eget elementum augue rhoncus. Sed et porta mauris. Donec suscipit convallis lacus, ut placerat ipsum sagittis et. In aliquet lorem nisi, eget condimentum dolor. Aenean tortor sapien, euismod ut sagittis eu, sollicitudin pretium lacus. In tincidunt, ligula ut hendrerit ullamcorper, justo felis hendrerit tortor, vitae placerat odio lorem vestibulum diam. Nullam sed nibh ac erat tincidunt fermentum id eu justo. Fusce hendrerit odio a turpis lacinia ultricies. Etiam ullamcorper, dui eu interdum hendrerit, odio enim tempor lorem, ut sagittis purus odio ut purus. Cras vitae ante et tortor semper varius ac sit amet libero. Integer vel ipsum sit amet tellus vestibulum euismod at vitae dui.</p>
<div class="abs deck" role="img" aria-label="DJ mixing controller with turntable"></div>
<div class="abs rule"></div>

<!-- Recent gigs -->
<h2 class="abs col-title serif" style="left:77px">Recent Gigs</h2>
<div class="abs view-all" style="left:286px">View all <i></i></div>
<div class="abs card" style="left:77px;top:738px"><div class="abs thumb" role="img" aria-label="DJ at decks video still" style="background:linear-gradient(135deg,#6a2a2a,#1a1a1a)"><div class="abs play"></div></div><p class="abs card-text">Cras vitae ante et tortor semper<br>varius ac sit amet libero. Integer<br>vestibulum euismod vitae.</p><span class="abs card-date">Jun-05-2013</span></div>
<div class="abs card" style="left:77px;top:840px"><div class="abs thumb" role="img" aria-label="Club crowd video still" style="background:linear-gradient(135deg,#777,#111)"><div class="abs play"></div></div><p class="abs card-text">Cras vitae ante et tortor semper<br>varius ac sit amet libero. Integer<br>vestibulum euismod vitae.</p><span class="abs card-date">Jun-05-2013</span></div>
<div class="abs card" style="left:77px;top:942px"><div class="abs thumb" role="img" aria-label="Purple stage lights video still" style="background:linear-gradient(135deg,#8a3ad0,#2a1050)"><div class="abs play"></div></div><p class="abs card-text">Cras vitae ante et tortor semper<br>varius ac sit amet libero. Integer<br>vestibulum euismod vitae.</p><span class="abs card-date">Jun-05-2013</span></div>

<!-- Upcoming gigs -->
<h2 class="abs col-title serif" style="left:380px">Upcoming Gigs</h2>
<div class="abs view-all" style="left:588px">View all <i></i></div>
<div class="abs card" style="left:380px;top:738px"><div class="abs thumb" role="img" aria-label="Black and white DJ video still" style="background:linear-gradient(135deg,#888,#111)"><div class="abs play"></div></div><p class="abs card-text">Cras vitae ante et tortor semper<br>varius ac sit amet libero. Integer<br>vestibulum euismod vitae.</p><span class="abs card-date">Jun-05-2013</span></div>
<div class="abs card" style="left:380px;top:840px"><div class="abs thumb" role="img" aria-label="DJ with headphones video still" style="background:linear-gradient(135deg,#bbb,#444)"><div class="abs play"></div></div><p class="abs card-text">Cras vitae ante et tortor semper<br>varius ac sit amet libero. Integer<br>vestibulum euismod vitae.</p><span class="abs card-date">Jun-05-2013</span></div>
<div class="abs card" style="left:380px;top:942px"><div class="abs thumb" role="img" aria-label="Event poster video still" style="background:linear-gradient(135deg,#a04020,#1a0a05)"><div class="abs play"></div></div><p class="abs card-text">Cras vitae ante et tortor semper<br>varius ac sit amet libero. Integer<br>vestibulum euismod vitae.</p><span class="abs card-date">Jun-05-2013</span></div>

<!-- Pagelinker feed -->
<div class="abs social-mark"></div>
<h2 class="abs col-title serif social" style="left:716px">Pagelinker feed</h2>
<div class="abs view-all" style="left:890px">View all <i></i></div>
<div class="abs card" style="left:682px;top:738px"><div class="abs thumb" role="img" aria-label="Fan profile photo" style="background:linear-gradient(135deg,#c89070,#6a4a60)"></div><p class="abs card-text">Cras vitae ante et tortor semper<br><a href="#">http//wwwsitename.com</a>&nbsp; Integer<br>vestibulum euismod vitae.</p><span class="abs card-meta">Jun-05-2013 &nbsp;:: &nbsp;Comment &nbsp;:: &nbsp;Like</span></div>
<div class="abs card" style="left:682px;top:840px"><div class="abs thumb" role="img" aria-label="Fan profile photo" style="background:linear-gradient(135deg,#ddd,#7a8aa0)"></div><p class="abs card-text">Cras vitae ante et tortor semper<br><a href="#">http//wwwsitename.com</a>&nbsp; Integer<br>vestibulum euismod vitae.</p><span class="abs card-meta">Jun-05-2013 &nbsp;:: &nbsp;Comment &nbsp;:: &nbsp;Like</span></div>
<div class="abs card" style="left:682px;top:942px"><div class="abs thumb" role="img" aria-label="Fan profile photo" style="background:linear-gradient(135deg,#f0c020,#c03040)"></div><p class="abs card-text">Cras vitae ante et tortor semper<br><a href="#">http//wwwsitename.com</a>&nbsp; Integer<br>vestibulum euismod vitae.</p><span class="abs card-meta">Jun-05-2013 &nbsp;:: &nbsp;Comment &nbsp;:: &nbsp;Like</span></div>

<!-- Famous gigs bar -->
<section class="abs famous">
  <div class="abs famous-label serif">Famous Gigs</div>
  <div class="abs famous-text">Cras vitae ante et tortor by Marek Holt &nbsp;:: &nbsp;Jun-05-2013</div>
  <div class="abs player">
    <svg class="abs" style="left:20px;top:6px" width="14" height="14"><path d="M2 1l11 6-11 6z" fill="#888"/></svg>
    <svg class="abs" style="left:64px;top:7px" width="16" height="12"><path d="M1 4h3l4-3v10L4 8H1z" fill="#777"/><path d="M11 3q2 3 0 6" stroke="#777" fill="none"/></svg>
    <div class="abs player-time">0:00 <span>/ 2:41</span></div>
  </div>
  <div class="abs btn" style="left:712px;width:62px"><b></b>Like</div>
  <div class="abs btn" style="left:774px;width:34px"><b style="background:#555"></b></div>
  <div class="abs btn" style="left:808px;width:52px">Share</div>
</section>

<footer class="abs footer">
  <div class="abs footer-links">Home &nbsp;| &nbsp;About us &nbsp;| &nbsp;Gigs &nbsp;| &nbsp;Contact us</div>
  <div class="abs footer-copy">Copyright &copy; 2013 &nbsp; www.djvorn.example &nbsp;All rights reserved.</div>
  <a class="abs footer-icon" href="https://www.pagelinker.example/pages/DJ-Vorn/730162948415207" aria-label="Pagelinker" style="left:899px;background:var(--social)"></a>
  <a class="abs footer-icon" href="#" aria-label="Tunedrift" style="left:926px;background:#f26a1b"></a>
</footer>

</body>
</html>
```